New concept travel "Fun" for young people !
----- Lingo Converter ----
With our skills, our agency was the first to develop spring break concepts in French-speaking Belgium by bringing together hundreds of students in Spain to celebrate!
Following a concern for health, our usual graphic designer can not take care of our achievements.
We are looking for a person in the long term (= serious work, contact exchanges and other "contracts").
We will also need a socialbook cover and a single-sided A4 poster.
The name of the concept is GOLDEN DRIFT.
You will be free to create a beautiful new logo of course.
This one could possibly be put on future t-shirts for our staff of animators during the trip or offered to the public!
Here is the job to do:
- Objective NEW CONCEPT 2018 in Bulgaria -
We need a visual (efficient and dynamic flyer to attract a population between 21 and 35 years old.
Flyer idea: A6 landscape postcard format, vintage, with a beautiful visual on the front that makes you want and arouse curiosity (with title of the trip "GOLDEN DRIFT - Bulgaria 2018") and the mention "New Concept" with our logo MORALIX TOURS .
On the back, on the left half of the postcard: a sweet little word from a woman, the style "Hey ! Le soleil est bien là, les cocktails sont savoureux et l'ambiance incroyable ! On t'attends avec les filles ! Je t'embrasse. Nora" with a fake kiss (= smack).
On the right half, useful information to stay to know:
- du samedi 1 au samedi 8 septembre 2018
- Plages Céleste, Bulgarie
- Voyage "tout compris" : vol aller-retour, hôtel 4**** formule ALL INCLUSIVE, entrées en boites, cocktails offerts, beach party, ... & bien plus !
- prix : € 599,00 par personne en chambre double
- plus d'infos sur www.golden-drift-trips.com ou au 0472 818 604
Here is the logo of our agency + some visuals of our last trip to Hungary (just to give you a little effect to feel ATTENTION I want something else here not copy please, please)
Good luck to everyone !

```html
<!DOCTYPE html>
<html lang="fr">
<head>
<meta charset="utf-8">
<title>Golden Drift – Bulgarie 2018</title>
<link rel="stylesheet" href="https://fonts.googleapis.com/css2?family=Oswald:wght@500;700&family=Silkscreen:wght@700&family=Dancing+Script:wght@600&family=Roboto+Condensed:wght@400;700&display=swap">
<style>
  :root {
    --paper: #ffffff;
    --ink: #111111;
    --rust: #c0622a;
    --rust-dark: #a9521f;
    --orange: #e8782a;
    --orange-edge: #e07127;
    --note: #c36d3c;
    --divider: #cfcfcf;
    --blue: #2a8fd8;
    --blue-light: #3fa9ec;
  }
  * { margin: 0; padding: 0; box-sizing: border-box; }
  html, body { width: 1200px; height: 848px; overflow: hidden; background: var(--paper); }
  .postcard {
    position: relative;
    width: 1200px;
    height: 848px;
    background: linear-gradient(to right, var(--paper) 0%, var(--paper) 72%, #f8d3b5 88%, var(--orange-edge) 100%);
    font-family: "Oswald", sans-serif;
    color: var(--ink);
  }
  .agency {
    position: absolute; left: 14px; top: 14px;
    display: flex; align-items: center; gap: 12px;
  }
  .agency-mark { width: 26px; height: 26px; background: var(--ink); }
  .agency-name { font-family: "Oswald", sans-serif; font-weight: 700; font-size: 38px; letter-spacing: 1px; color: var(--ink); }

  .divider {
    position: absolute; left: 580px; top: 86px; height: 715px;
    border-left: 2px solid var(--divider);
  }

  .note {
    position: absolute; left: 40px; top: 160px; width: 520px;
    font-family: "Dancing Script", cursive;
    font-weight: 600; font-size: 42px; line-height: 76px;
    color: var(--note);
    transform: rotate(-4deg);
    transform-origin: left top;
  }
  .note .sign { padding-left: 120px; margin-top: 20px; display: block; }
  .kiss { position: absolute; left: 335px; top: 612px; width: 165px; height: 84px; }

  .dates {
    position: absolute; left: 650px; top: 8px; width: 500px; height: 120px;
    background: var(--rust);
    border-radius: 16px 16px 60px 60px / 16px 16px 40px 40px;
    color: #fff; text-align: center;
  }
  .dates .days { font-family: "Roboto Condensed", sans-serif; font-size: 30px; padding-top: 6px; }
  .dates .month { font-family: "Oswald", sans-serif; font-weight: 700; font-size: 50px; line-height: 60px; }

  .info { position: absolute; left: 640px; width: 520px; text-align: center; }
  .resort { top: 148px; font-family: "Silkscreen", sans-serif; font-weight: 700; font-size: 34px; letter-spacing: 3px; }
  .country { top: 200px; font-family: "Silkscreen", sans-serif; font-weight: 700; font-size: 62px; letter-spacing: 4px; }
  .features {
    top: 298px; list-style: none;
    font-family: "Oswald", sans-serif; font-weight: 500; font-size: 31px; line-height: 42.5px;
    text-transform: uppercase;
  }
  .features .accent { color: var(--orange); }

  .price {
    position: absolute; left: 756px; top: 640px; width: 290px; height: 64px;
    background: var(--rust-dark); border-radius: 32px;
    color: #fff; font-family: "Oswald", sans-serif; font-weight: 700; font-size: 34px;
    text-align: center; line-height: 60px;
  }
  .price-note {
    position: absolute; left: 990px; top: 694px; width: 130px;
    font-family: "Roboto Condensed", sans-serif; font-size: 15px; line-height: 17px; text-align: center;
  }

  .contact { position: absolute; left: 756px; top: 730px; width: 372px; height: 108px; }
  .contact svg { position: absolute; inset: 0; }
  .contact-text {
    position: relative; padding: 10px 50px 0 8px; text-align: center; color: #fff;
    font-family: "Roboto Condensed", sans-serif; font-weight: 700; font-size: 20px; line-height: 29px;
  }
</style>
</head>
<body>
<main class="postcard">
  <div class="agency"><span class="agency-mark"></span><span class="agency-name">MORALIX TOURS</span></div>

  <div class="divider"></div>

  <p class="note">
    Hey ! Le soleil est bien là,<br>
    les cocktails sont savoureux<br>
    et l'ambiance incroyable !<br>
    On t'attends avec les filles !<br>
    Je t'embrasse…
    <span class="sign">Nora.</span>
  </p>

  <svg class="kiss" viewBox="0 0 165 84" role="img" aria-label="Lipstick kiss mark">
    <defs>
      <radialGradient id="kissTone" cx="50%" cy="50%" r="55%">
        <stop offset="0%" stop-color="#d2336e"/>
        <stop offset="100%" stop-color="#a2154a"/>
      </radialGradient>
    </defs>
    <ellipse cx="82" cy="42" rx="80" ry="38" fill="url(#kissTone)"/>
  </svg>

  <div class="dates">
    <p class="days">Du samedi 1 au samedi 8</p>
    <p class="month">septembre 2018</p>
  </div>

  <h2 class="info resort">PLAGES CÉLESTE</h2>
  <h1 class="info country">BULGARIE</h1>

  <ul class="info features">
    <li>Voyage "tout compris"</li>
    <li>Vol aller-retour</li>
    <li>Hôtel 4****</li>
    <li class="accent">Formule all inclusive</li>
    <li>Entrées en boites</li>
    <li>Cocktails offerts</li>
    <li>Beach party</li>
    <li class="accent">… &amp; bien plus</li>
  </ul>

  <div class="price">PRIX : € 599,00</div>
  <p class="price-note">par personne<br>en chambre double</p>

  <div class="contact">
    <svg viewBox="0 0 372 108" preserveAspectRatio="none" aria-hidden="true">
      <defs>
        <linearGradient id="contactBlue" x1="0" y1="0" x2="1" y2="0">
          <stop offset="0%" stop-color="#1f82cf"/>
          <stop offset="100%" stop-color="#49b3f0"/>
        </linearGradient>
      </defs>
      <path d="M0 0 H318 L372 54 L318 108 H0 Z" fill="url(#contactBlue)"/>
    </svg>
    <p class="contact-text">Plus d'infos sur :<br>www.golden-drift-trips.com<br>0472 818 604</p>
  </div>
</main>
</body>
</html>
```